Fern Vale Ridgecrest Music Festival Poster

We are a summer music festival with concerts spanning Jazz, Cabaret, Education, Broadway, Chamber and Opera. We are looking for our key art for the 2016 season. This design will serve as the basis for all promotional materials, the concert program, and our web materials. Though eventually this means we will need to adjust the design to fit many different sizes, our poster will be printed mostly on 8.5" x 11" paper, and we can adapt from there. The design will be featured online and in print. It should be vertical and not landscape.

WE ARE SEEKING SLEEK, ELEGANT DESIGNS WITH MAYBE A KEY STOCK PHOTOGRAPH AND THE RELEVANT TEXT/DETAILS.

PLEASE NOTE: The included file "avenir logo.psd" is just a suggestion for the feel we are going for. It is our "working logo" after having scraped our old logo. We are interested in seeing your own ideas on how to style the brand name, but if you have ideas working with this version of the logo, feel free to use it.

REQUIRED DETAILS:
Festival Name: Fern Vale Ridgecrest Music Festival
Dates: July 29 - August 7 2016 (the year, 2016, must be included on the poster, but it does not need to be in the same location as where the actual dates are listed)
Website: www.fernvaleridgecrestfest.org

Additional Information:
- the 7 musical styles (jazz, choral, cabaret, education, broadway, chamber, opera) are important to defining who we are. You may decide to include these on the poster.
- We are looking for a very elegant design

TARGET:
We depend highly on an older clientele. We are working to expand our brand into younger demographics, but we want to be sure that we do not alienate our current consumer base with text that may be difficult for them to read.

Project Deadline Extended Reason: I am extending the deadline because it is taking longer to get feedback from my superiors than I had expected. Extending the deadline will give me time to provide adequate feedback from the people who will ultimately be making the decision. Thank you. Added Saturday, January 30, 2016

Sorry for the delay. There were issues with the decision makers but we are selecting in the next 24 hours.

Target Market(s)

Lovers of the styles of music we feature. We have a good number of elderly consumers, but also families and school groups (discussed further in description section)

Industry/Entity Type

Entertainment

Font styles to use
Sans Serif

Requirements
Must have
• Festival Name: Fern Vale Ridgecrest Music Festival
• Dates: July 29 - August 7 2016 (the year, 2016, must be included on the poster, but it does not need to be in the same location as where the actual dates are listed)
• Website: www.fernvaleridgecrestfest.org
Nice to have
• - the 7 musical styles (jazz, choral, cabaret, education, broadway, chamber, opera) are important to defining who we are. We would love to include these styles somewhere on the image, or feature them somehow in the artwork
• - Our brand has an elegance to it due to the type of music we offer, and our location being in a very natural space. inclusion of the music/nature mixed aspect of our brand in artwork might be nice
Should not have
• Anything that may offend or alienate an older, more conservative demographic

```html
<!DOCTYPE html>
<html lang="en">
<head>
<meta charset="utf-8">
<title>Fern Vale Ridgecrest Music Festival 2016</title>
<link href="https://fonts.googleapis.com/css2?family=Raleway:wght@200;300&family=Montserrat:wght@800&family=Great+Vibes&family=Oswald:wght@500&display=swap" rel="stylesheet">
<style>
  :root {
    --sky-top: #27366b;
    --sky-mid: #3f5fc4;
    --sky-light: #5a8ad6;
    --forest-haze: #2f9a8c;
    --forest: #1d6a47;
    --forest-deep: #0e3221;
    --ink: #ffffff;
    --ink-soft: #eef1f6;
    --date-accent: #f6f0a2;
    --moon: rgba(255, 255, 255, 0.17);
  }
  html, body { margin: 0; padding: 0; overflow: hidden; background: var(--forest-deep); }
  .poster {
    position: relative;
    width: 860px;
    height: 1200px;
    overflow: hidden;
    color: var(--ink);
    font-family: 'Raleway', sans-serif;
  }
  .scenery {
    position: absolute; inset: 0;
    background: linear-gradient(180deg,
      var(--sky-top) 0%,
      var(--sky-mid) 22%,
      var(--sky-light) 40%,
      var(--forest-haze) 62%,
      var(--forest) 80%,
      var(--forest-deep) 100%);
  }
  .moon { position: absolute; left: 0; top: 0; }
  .tagline-band {
    position: absolute; left: 0; right: 0; top: 35px; height: 39px;
    border-top: 1px solid rgba(255,255,255,0.75);
    border-bottom: 1px solid rgba(255,255,255,0.75);
    display: flex; align-items: center; justify-content: center;
  }
  .tagline {
    margin: 0; font-weight: 300; font-size: 16px; letter-spacing: 0.42em;
    text-transform: uppercase; padding-left: 0.42em;
  }
  .genres {
    position: absolute; left: 0; right: 0; top: 90px;
    text-align: center; font-weight: 200; font-size: 45px; line-height: 50px;
    text-transform: uppercase; margin: 0;
  }
  .genres span { margin: 0 14px; }
  .title {
    position: absolute; left: 0; right: 0; top: 385px; margin: 0;
    text-align: center; font-family: 'Montserrat', sans-serif; font-weight: 800;
    text-transform: uppercase; color: var(--ink-soft);
    text-shadow: 2px 3px 3px rgba(20, 40, 70, 0.45);
  }
  .title-top { display: block; font-size: 88px; line-height: 92px; letter-spacing: -3px; }
  .title-main { display: block; font-size: 104px; line-height: 118px; letter-spacing: -4px; }
  .subtitle {
    position: absolute; left: 0; right: 0; top: 598px; margin: 0;
    text-align: center; font-family: 'Great Vibes', cursive; font-weight: 400;
    font-size: 92px; line-height: 110px;
    text-shadow: 1px 2px 3px rgba(10, 60, 60, 0.5);
  }
  .dates {
    position: absolute; left: 0; right: 0; top: 762px; margin: 0;
    text-align: center; font-family: 'Oswald', sans-serif; font-weight: 500;
    text-transform: uppercase; text-shadow: 1px 2px 2px rgba(0,0,0,0.35);
  }
  .dates-range { display: block; font-size: 46px; line-height: 58px; transform: scaleY(1.15); }
  .dates-range .day { color: var(--date-accent); font-size: 56px; }
  .dates-year { display: block; font-size: 32px; line-height: 40px; }
  .website {
    position: absolute; left: 0; right: 0; top: 1118px; margin: 0;
    text-align: center; font-weight: 300; font-size: 21px; letter-spacing: 0.36em;
    padding-left: 0.36em; text-transform: uppercase;
  }
</style>
</head>
<body>
<main class="poster">
  <div class="scenery" role="img" aria-label="Misty evening sky over a silhouetted pine forest and grassy hillside"></div>
  <svg class="moon" width="860" height="1200" viewBox="0 0 860 1200" aria-hidden="true">
    <circle cx="430" cy="600" r="348" fill="var(--moon)"/>
  </svg>

  <header class="tagline-band">
    <p class="tagline">In the majestic Alder Ridge Mountains</p>
  </header>

  <p class="genres">
    <span>Jazz</span> <span>Choral</span> <span>Cabaret</span> <span>Opera</span><br>
    <span>Education</span> <span>Broadway</span> <span>Chamber</span>
  </p>

  <h1 class="title">
    <span class="title-top">Fern Vale</span>
    <span class="title-main">Ridgecrest</span>
  </h1>
  <p class="subtitle">Music Festival</p>

  <p class="dates">
    <span class="dates-range"><span class="day">29</span> July - <span class="day">7</span> August</span>
    <span class="dates-year">2016</span>
  </p>

  <p class="website">www.fernvaleridgecrestfest.org</p>
</main>
</body>
</html>
```